Corporate Website for Harbor Signal
Landing Page + Rotating Banner (3) Designs
Thanks to all who took part in this design brief. Your collective creative instincts made it difficult for us to finalize a concept. Congratulations go to tuvelsk42 who for us developed a fitting image for the Harbor Signal web site.
It has been a very rewarding process for us as it has displayed a viable avenue for future web design sourcing and we hope to work with you all again soon.
Kind Regards
Odrey
Ok we've got a few designers still in and most have managed to fulfil the brief requirements with some nice clean layouts a colour combinations. We're just looking for the correct theme/background to accompany the content. If I don't see any development on this by tomorrow, I will extend the project by a few days to give you time to develop your concepts. Remember not too bold, just something to subtly occupy the white space behind the main template.
Thank you for your efforts so far.
Hi Brightfold
I like your subtle use of colour on the menu and how it ties in with the logo. (I have attached our logo to this brief, please apply this to your next draft). Can you try a different colour concept for the top bar behind the logo.
The shadow cast by the page is also a nice touch but for your next draft can we see more reference to the industry as inspiration for the background concept i.e. "digital", "technology", "electronics" etc.(faded, not to prominent).
Can you change the promotional banner to contain just one image concept of your own ( not too complicated, just fill the space with a fitting mood ). Also can you make better use of the space on the lower half of the page.
Thank you for your submission.
Just to clarify to all those wishing to develop for this design brief, we are mainly looking for an elegant sophisticated landing page, the 3 banner designs are secondary to this.
Hi salvemora
The reason I have given a one star rating is based on the brief requirements.
We are looking for a clean professional corporate landing page. We find the use of font size and colour in your submission does not represent our needs. A better use of white space and typography and less emphasis on full colour background would boost your submissions appeal.
Please view the example websites as a guide and also incorporate our logo provided to help with colour concepts.
Thanks again for your entry.

```html
<!DOCTYPE html>
<html lang="en">
<head>
<meta charset="utf-8">
<title>Harbor Signal</title>
<link href="https://fonts.googleapis.com/css2?family=Open+Sans:wght@400;600;700&display=swap" rel="stylesheet">
<style>
:root{
  --bg:#ececec;
  --page:#ffffff;
  --ink:#444444;
  --muted:#777777;
  --blue:#1f8ad6;
  --blue-dark:#1a5f91;
  --banner-top:#7fa3c2;
  --banner-bot:#4f7ea6;
  --nav:#efefef;
  --line:#d8d8d8;
  --band:#e6e6e6;
  --footer:#e3e3e3;
}
*{margin:0;padding:0;box-sizing:border-box}
html,body{width:1200px;height:1045px;overflow:hidden}
body{background:var(--bg);font-family:"Open Sans",Arial,sans-serif;color:var(--ink);position:relative}
.page{position:absolute;left:150px;top:0;width:900px;height:918px;background:var(--page);box-shadow:0 0 18px rgba(0,0,0,.12)}
.abs{position:absolute}
.brand{left:168px;top:26px;display:flex;align-items:center;gap:10px;font-size:26px;font-weight:700;color:var(--blue-dark)}
.brand .dot{width:22px;height:22px;border-radius:50%;background:var(--blue)}
.toplinks{right:168px;top:24px;font-size:13px;color:var(--blue)}
.toplinks span{color:var(--muted);margin:0 4px}
.phone{right:168px;top:50px;font-size:24px;color:var(--blue-dark);display:flex;align-items:center;gap:8px}
.nav{left:164px;top:107px;width:872px;height:40px;background:var(--nav);border:1px solid var(--line);display:flex}
.nav a{display:block;height:38px;line-height:38px;font-size:14px;font-weight:600;color:#333;text-decoration:none;text-align:center;border-right:1px solid var(--line)}
.nav a.w1{width:90px}.nav a.w2{width:116px}.nav a.w3{width:106px}.nav a.w4{width:96px}.nav a.w5{width:130px}.nav a.w6{width:100px}
.nav a.active{background:var(--blue);color:#fff}
.search{margin:7px 0 0 14px;width:190px;height:24px;background:#fff;border:1px solid #ccc;border-radius:12px;font-size:12px;color:#999;line-height:22px;padding-left:10px;position:relative}
.search svg{position:absolute;right:8px;top:5px}
.banner{left:164px;top:155px;width:872px;height:269px;background:linear-gradient(180deg,var(--banner-top),var(--banner-bot));overflow:hidden}
.banner h1{position:absolute;left:30px;top:30px;font-size:24px;font-weight:700;color:#fff}
.banner p{position:absolute;left:30px;top:70px;width:370px;font-size:12px;line-height:17px;color:#eef4fa}
.readmore{position:absolute;left:30px;top:152px;background:#f4f4f4;color:#333;font-size:13px;font-weight:600;padding:4px 14px;border-radius:3px}
.product{position:absolute;left:440px;top:20px;width:410px;height:230px;border-radius:10px;background:linear-gradient(135deg,#c9d6e0,#a9855c 55%,#eaeaea)}
.dots{position:absolute;left:30px;top:243px;display:flex;gap:8px}
.dots i{width:9px;height:9px;border-radius:50%;background:#d6e2ec;display:block}
.dots i.on{background:#fff}
.strip{left:164px;top:430px;width:872px;height:52px;background:linear-gradient(#f7f7f7,#e6e6e6);border:1px solid var(--line)}
.strip p{position:absolute;left:28px;top:17px;font-size:12px;color:#555}
.strip svg{position:absolute;right:30px;top:8px}
.card{top:514px;width:276px;height:183px}
.card .rule{height:4px;background:linear-gradient(90deg,var(--line),#bdbdbd)}
.card .pic{position:absolute;left:10px;top:14px;width:108px;height:100px}
.card .txt{position:absolute;left:130px;top:14px;width:140px;font-size:11px;line-height:15px;color:#555}
.card .band{position:absolute;left:0;bottom:0;width:100%;height:58px;background:linear-gradient(#f4f4f4,var(--band));border:1px solid var(--line);border-radius:0 0 6px 6px}
.card .band b{position:absolute;left:18px;top:20px;font-size:18px;color:var(--blue-dark)}
.card .band em{position:absolute;right:22px;top:8px;font-style:normal;font-size:11px;color:#666}
.card .band em u{text-decoration:none;color:var(--blue)}
.news{left:182px;top:730px;width:255px}
.news li{list-style:none;position:relative;padding-left:12px;font-size:11px;line-height:15px;color:#444;margin-bottom:14px}
.news li:before{content:"";position:absolute;left:0;top:5px;border:4px solid transparent;border-left-color:var(--blue)}
.news li span{display:block;color:var(--blue);font-size:10px}
.about{left:463px;top:728px;width:568px;font-size:11px;line-height:15px;color:#555}
.about p+p{margin-top:10px}
.label{top:861px;height:37px;background:linear-gradient(#f4f4f4,var(--band));border:1px solid var(--line);border-radius:0 0 6px 6px;font-size:18px;font-weight:700;color:var(--blue-dark);line-height:35px;padding-left:16px}
.footer{left:0;top:918px;width:1200px;height:127px;background:var(--footer)}
.flinks{left:168px;top:942px;font-size:11px;color:#444}
.flinks span{margin:0 5px;color:#999}
.copy{left:168px;top:966px;font-size:11px;color:#555}
.fbrand{right:165px;top:948px;display:flex;align-items:center;gap:6px;font-size:16px;font-weight:700;color:var(--blue-dark)}
.fbrand .dot{width:12px;height:12px;border-radius:50%;background:var(--blue)}
.social{right:165px;top:1002px;display:flex;gap:6px}
.social i{display:block;width:18px;height:18px;border-radius:3px}
</style>
</head>
<body>
<div class="page"></div>

<div class="abs brand"><span class="dot"></span>Harbor Signal</div>
<div class="abs toplinks">Welcome<span>|</span>Help<span>|</span>FAQ</div>
<div class="abs phone">
  <svg width="20" height="20" viewBox="0 0 24 24"><path d="M6.6 10.8a15 15 0 0 0 6.6 6.6l2.2-2.2a1 1 0 0 1 1-.25 11 11 0 0 0 3.6.6 1 1 0 0 1 1 1V20a1 1 0 0 1-1 1A17 17 0 0 1 3 4a1 1 0 0 1 1-1h3.5a1 1 0 0 1 1 1 11 11 0 0 0 .6 3.6 1 1 0 0 1-.25 1z" fill="#1a5f91"/></svg>
  000-000-1234
</div>

<nav class="abs nav">
  <a class="w1">Home</a><a class="w2 active">About Us</a><a class="w3">Products</a><a class="w4">Preset</a><a class="w5">Where To Buy</a><a class="w6">Contact</a>
  <div class="search">Search...
    <svg width="13" height="13" viewBox="0 0 14 14"><circle cx="6" cy="6" r="4.5" fill="none" stroke="#888" stroke-width="1.6"/><line x1="9.3" y1="9.3" x2="13" y2="13" stroke="#888" stroke-width="1.8"/></svg>
  </div>
</nav>

<section class="abs banner">
  <h1>Harbor Signal</h1>
  <p>Fast, secure wireless access that travels with you. Plug in, connect in seconds and stay online wherever the day takes you, at home, at work or on the road.</p>
  <div class="readmore">Read More</div>
  <div class="product" role="img" aria-label="Wood-finished USB wireless modem stick"></div>
  <div class="dots"><i class="on"></i><i></i><i></i><i></i></div>
</section>

<div class="abs strip">
  <p>Harbor Signal keeps you connected with simple plans, clear pricing and reliable coverage across the region.</p>
  <svg width="40" height="36" viewBox="0 0 40 36"><rect x="4" y="4" width="30" height="26" fill="#fff" stroke="#888" stroke-width="1.5" transform="rotate(-6 19 17)"/><g stroke="#999" stroke-width="1.5" transform="rotate(-6 19 17)"><line x1="9" y1="10" x2="29" y2="10"/><line x1="9" y1="15" x2="29" y2="15"/><line x1="9" y1="20" x2="29" y2="20"/><line x1="9" y1="25" x2="22" y2="25"/></g></svg>
</div>

<div class="abs card" style="left:164px">
  <div class="rule"></div>
  <div class="pic" role="img" aria-label="Black network peripheral device" style="background:linear-gradient(135deg,#e8e8e8,#2a2a2a)"></div>
  <div class="txt">Cables, adapters and chargers built to pair with every Harbor Signal device you own.</div>
  <div class="band"><b>Pereferals</b><em>Click <u>Here</u></em></div>
</div>
<div class="abs card" style="left:460px">
  <div class="rule"></div>
  <div class="pic" role="img" aria-label="Blue network cables and connectors" style="background:linear-gradient(135deg,#eef2f5,#3d6fa0)"></div>
  <div class="txt">Protect your network with smart encryption and alerts that watch over your data.</div>
  <div class="band"><b>Security</b><em>Click <u>Here</u></em></div>
</div>
<div class="abs card" style="left:762px">
  <div class="rule"></div>
  <div class="pic" role="img" aria-label="Hands raised holding mobile devices against the sky" style="background:linear-gradient(180deg,#b9cfe2,#8a6f5a)"></div>
  <div class="txt">Share one fast connection with friends anywhere you go, no setup needed.</div>
  <div class="band"><b>Mobile Wi- Fi</b><em>Click <u>Here</u></em></div>
</div>

<ul class="abs news">
  <li>Do your layouts deserve better than Lorem Ipsum? Apply as an art director and learn<span>09.oct.2011</span></li>
  <li>Do your layouts deserve better than Lorem Ipsum? Apply as an art director and learn<span>09.oct.2011</span></li>
</ul>

<div class="abs about">
  <p>Harbor Signal began with a simple idea: wireless access should be easy, fair and always there when you need it. Today our network serves homes, offices and travellers across the coast, backed by a support team that answers quickly and speaks plainly.</p>
  <p>We build our own devices, test every plan in the field and keep pricing clear, so you spend less time on setup and more time online.</p>
</div>

<div class="abs label" style="left:164px;width:276px">Latest News</div>
<div class="abs label" style="left:460px;width:576px">Who We Are</div>

<footer class="abs footer"></footer>
<div class="abs flinks">Home<span>|</span>About Us<span>|</span>Products<span>|</span>Preset<span>|</span>Where To Buy<span>|</span>Contact</div>
<div class="abs copy">© Copyright 2011, Harbor Signal. All Rightsreserved</div>
<div class="abs fbrand"><span class="dot"></span>Harbor Signal</div>
<div class="abs social"><i style="background:#3b5a98"></i><i style="background:#33b5e5"></i><i style="background:#f08a24"></i><i style="background:#2d8fd5"></i></div>
</body>
</html>
```